Academy Values Classroom Poster

Marrowby Community Academy has the core values of Aspiration, Positivity, Responsibility and Achievement at its heart. We have these words displayed in our entrance (in Bliss font) but would like them to permeate into the classroom spaces in a poster form. We want a clear message that shows what the values mean to students:

Aspiration - Think BIG (pantone 717)
Positivity - Smile :-) (pantone 376)
Responsibility - for yourself and others (pantone 569)
Achievement - Celebrate Success! (pantone 214)

It would be good to follow the colour scheme of the main words to create a 'brand' for these values (pantone refs noted in brackets) and we would like to see some clean designs please.

I anticipate these will be A1 posters.

I have attached our school logo although it is not essential that this is included.

Target Market(s)

Students

Industry/Entity Type

School

Font styles to use
Other font styles liked:
• Bliss or Segoe UI

Requirements
Must have
• Aspiration - Think BIG
Positivity - Smile :-)
Responsibility - for yourself and others
Achievement - Celebrate Success!
Should not have
• Nothing too busy

```html
<!DOCTYPE html>
<html lang="en">
<head>
<meta charset="utf-8">
<title>Academy Values Posters</title>
<link rel="stylesheet" href="https://fonts.googleapis.com/css2?family=Anton&family=Bebas+Neue&family=Josefin+Sans:wght@600;700&family=Oswald:wght@500;700&display=swap">
<style>
  :root {
    --wall: #dedede;
    --paper: #f7f7f5;
    --frame-black: #111111;
    --teal: #1f9b8b;
    --teal-deep: #1c6f66;
    --ink: #1e2b2b;
    --red: #e5343d;
    --green: #4db53b;
    --pink: #e02a80;
    --yellow: #f3ea2a;
    --orange: #f29a22;
    --white: #ffffff;
  }
  * { box-sizing: border-box; }
  html, body {
    margin: 0;
    width: 1200px;
    height: 778px;
    overflow: hidden;
    background: var(--wall);
  }
  .poster-row {
    position: absolute;
    left: 36px;
    top: 202px;
    display: flex;
    gap: 24px;
  }
  .poster {
    width: 264px;
    height: 342px;
    padding: 12px;
  }
  .poster--white-frame { background: var(--paper); }
  .poster--black-frame { background: var(--frame-black); padding: 20px; }
  .poster__field {
    width: 100%;
    height: 100%;
    display: flex;
    flex-direction: column;
    align-items: center;
    justify-content: center;
    text-align: center;
    line-height: 1;
  }
  .poster__field p { margin: 0; }

  /* Responsibility */
  .poster-responsibility .poster__field { background: var(--teal); gap: 14px; }
  .resp-label {
    font-family: "Josefin Sans", sans-serif;
    font-weight: 700;
    font-size: 15px;
    letter-spacing: 3px;
    color: var(--paper);
  }
  .resp-for {
    font-family: "Josefin Sans", sans-serif;
    font-weight: 700;
    font-size: 44px;
    letter-spacing: 8px;
    color: var(--paper);
  }
  .resp-yourself {
    font-family: "Josefin Sans", sans-serif;
    font-weight: 700;
    font-size: 28px;
    letter-spacing: 3px;
    color: var(--ink);
  }
  .resp-others {
    font-family: "Josefin Sans", sans-serif;
    font-weight: 700;
    font-size: 28px;
    letter-spacing: 2px;
    color: var(--red);
  }

  /* Positivity */
  .poster-positivity .poster__field { background: var(--green); gap: 6px; }
  .smile-main {
    font-family: "Bebas Neue", sans-serif;
    font-size: 104px;
    letter-spacing: 2px;
    color: var(--white);
  }
  .smile-face {
    font-family: "Bebas Neue", sans-serif;
    font-size: 40px;
    letter-spacing: 4px;
    color: var(--frame-black);
  }

  /* Achievement */
  .poster-achievement .poster__field { background: var(--pink); gap: 22px; }
  .celebrate {
    font-family: "Oswald", sans-serif;
    font-weight: 700;
    font-size: 44px;
    letter-spacing: 2px;
    color: var(--white);
  }
  .success {
    font-family: "Anton", sans-serif;
    font-size: 50px;
    letter-spacing: 1px;
    color: var(--yellow);
  }

  /* Aspiration */
  .poster-aspiration .poster__field { background: var(--orange); gap: 10px; }
  .think {
    font-family: "Oswald", sans-serif;
    font-weight: 700;
    font-size: 46px;
    letter-spacing: 4px;
    color: var(--white);
  }
  .big {
    font-family: "Anton", sans-serif;
    font-size: 130px;
    color: var(--teal-deep);
  }
</style>
</head>
<body>
<main class="poster-row">

  <section class="poster poster--white-frame poster-responsibility">
    <div class="poster__field">
      <p class="resp-label">RESPONSIBILITY</p>
      <p class="resp-for">FOR</p>
      <p class="resp-yourself">YOURSELF</p>
      <p class="resp-others">AND OTHERS</p>
    </div>
  </section>

  <section class="poster poster--black-frame poster-positivity">
    <div class="poster__field">
      <p class="smile-main">SMILE</p>
      <p class="smile-face">:-)</p>
    </div>
  </section>

  <section class="poster poster--white-frame poster-achievement">
    <div class="poster__field">
      <p class="celebrate">CELEBRATE</p>
      <p class="success">SUCCESS!</p>
    </div>
  </section>

  <section class="poster poster--black-frame poster-aspiration">
    <div class="poster__field">
      <p class="think">THINK</p>
      <p class="big">BIG</p>
    </div>
  </section>

</main>
</body>
</html>
```